Text heavy poster for university audience

I have developed a set of standards for online teaching that need to be turned into a post format. The project has a logo which should be incorporated. Most of the designing will be in terms of text layout. The logo (two versions - higher quality files available) and the a sample of standards (as image - word version available; the example is one third of standards) are attached. Design that can be adapted to brochure format would be great. (Brochure adaption will be paid separately via another project to be opened here). More details available here: http://www.brivelquarto.net
Updates

Dear all,

The URL for the site needs to be include in the design - either as footer or under logo:
<http://www.brivelquarto.net>

Sorry for late notice

Target Market(s)

The are university staff

Industry/Entity Type

University

Font styles to use
Serif
Sans Serif

Requirements
Must have
• The text in the "required" attachment must be included; but for initial draft feel free to restrict your design to "sample" attachment
The green from the Logo (PANTONE 17-5641 Emerald) should be the foundation of the colour palette.
Nice to have
• The collaborators as named here: http://www.brivelquarto.net/collaborators/
My preferred find is helvetica neue, but similar can be used
Should not have
• Decorative fonts

```html
<!DOCTYPE html>
<html lang="en">
<head>
<meta charset="utf-8">
<title>Brivel Quarto Standards – Online Teaching Poster</title>
<link rel="stylesheet" href="https://fonts.googleapis.com/css2?family=Arimo:wght@400;700&family=Tinos:wght@400;700&display=swap">
<style>
  :root {
    --emerald: #009b77;
    --emerald-dark: #0b6b55;
    --paper: #fdfaec;
    --frame: #8fd3c7;
    --cell: #c9dfd0;
    --rule: #2f3e38;
    --note: #f8efb2;
    --note-edge: #d9cd86;
    --ink: #1a1a1a;
    --title-cream: #fdf5c4;
    --title-yellow: #f3e680;
    --sans: "Arimo", "Helvetica Neue", Arial, sans-serif;
    --serif: "Tinos", "Times New Roman", serif;
  }
  * { box-sizing: border-box; margin: 0; padding: 0; }
  html, body { width: 848px; height: 1200px; overflow: hidden; background: #fff; }
  .poster {
    position: relative; width: 848px; height: 1200px;
    background: var(--paper); color: var(--ink); font-family: var(--sans);
  }
  .poster-frame {
    position: absolute; left: 27px; top: 27px; right: 27px; bottom: 27px;
    border: 1.5px solid var(--frame);
  }
  .masthead {
    position: absolute; left: 63px; top: 55px; width: 476px; height: 148px;
    background: var(--emerald); box-shadow: 2px 3px 4px rgba(0,0,0,.25);
    display: flex; align-items: center; padding-left: 40px; gap: 26px;
  }
  .masthead-mark { width: 64px; height: 64px; background: #fff; flex: none; }
  .masthead-name {
    color: #fff; font-weight: 700; font-size: 31px; line-height: 1.12; letter-spacing: .5px;
  }
  .credits {
    position: absolute; left: 555px; top: 57px; width: 238px; height: 146px;
    background: var(--note); box-shadow: 2px 3px 4px rgba(0,0,0,.2);
    text-align: center; padding: 8px 10px;
  }
  .credits-name { font-weight: 700; font-size: 17px; line-height: 1.15; }
  .credits-text { font-weight: 700; font-size: 11px; line-height: 1.3; margin-top: 5px; }
  .theme-box {
    background: var(--emerald); text-align: center; box-shadow: 2px 3px 4px rgba(0,0,0,.25);
    padding: 6px 8px;
  }
  .theme-title { color: var(--title-cream); font-size: 17px; font-weight: 400; line-height: 1.2; }
  .theme-summary { color: var(--title-yellow); font-size: 11.5px; font-weight: 700; line-height: 1.3; margin-top: 3px; }
  .theme-students { position: absolute; left: 63px; top: 217px; width: 476px; height: 97px; }
  .theme-organisation { position: absolute; left: 555px; top: 217px; width: 238px; height: 97px; }
  .theme-staff { width: 238px; height: 98px; margin: 16px 0 10px 2px; padding-top: 10px; }
  .column { position: absolute; top: 322px; }
  .col-a { left: 53px; width: 242px; }
  .col-b { left: 303px; width: 242px; }
  .col-c { left: 553px; width: 244px; }
  .standard { margin-bottom: 10px; }
  .standard h3 {
    font-size: 12.5px; font-weight: 700; line-height: 1.2; margin-bottom: 5px; padding-right: 4px;
  }
  .levels {
    width: 100%; border-collapse: collapse; background: var(--cell);
    font-family: var(--serif); font-size: 10px; line-height: 1.1;
    box-shadow: 1px 2px 2px rgba(0,0,0,.15);
  }
  .levels th, .levels td { border: 1px solid var(--rule); vertical-align: top; padding: 1px 2px; text-align: left; }
  .levels th { font-weight: 400; width: 53px; }
  .levels .excellent td { height: 12px; }
  .licence-mark { display: flex; align-items: center; justify-content: center; gap: 6px; margin: 12px 0 8px; }
  .licence-mark span.dot { width: 24px; height: 24px; border-radius: 50%; background: #111; }
  .licence-mark span.name { font-size: 22px; font-weight: 700; color: #111; }
  .licence-note {
    margin: 0 6px; background: var(--note); border: 1px solid var(--note-edge);
    box-shadow: 2px 3px 4px rgba(0,0,0,.2);
    font-size: 8px; line-height: 1.3; padding: 7px 10px 8px;
  }
  .licence-note p + p { margin-top: 8px; }
</style>
</head>
<body>
<main class="poster">
  <div class="poster-frame"></div>

  <header class="masthead">
    <span class="masthead-mark"></span>
    <div class="masthead-name">BRIVEL<br>QUARTO<br>STANDARDS</div>
  </header>

  <aside class="credits">
    <div class="credits-name">Dana Korwell<br>and Collaborators</div>
    <p class="credits-text">Because of the large number of collaborators who worked on this project, they are not listed here, but they may be viewed on our website: http://www.brivelquarto.net/ collaborators/</p>
  </aside>

  <section class="theme-box theme-students">
    <h2 class="theme-title">One: Students</h2>
    <p class="theme-summary">Students are supported in their online learning<br>with a quality curriculum [1-4],<br>opportunities for interaction with peers and staff [5&amp;6],<br>and appropriate support [7&amp;8].</p>
  </section>

  <section class="theme-box theme-organisation">
    <h2 class="theme-title">Three: Organisation</h2>
    <p class="theme-summary">The organisation supports online education through the provision of quality leadership [12-13], infrastructure [14] and evaluation [15-17]</p>
  </section>

  <div class="column col-a">
    <article class="standard">
      <h3>1. Curriculum materials are aligned, available and engaging</h3>
      <table class="levels">
        <tr><th>Threshold</th><td>The necessary materials are constructively aligned and available online</td></tr>
        <tr><th>Good</th><td>The materials are provided using a variety of media to engage students and support diversity</td></tr>
        <tr class="excellent"><th>Excellent</th><td></td></tr>
      </table>
    </article>
    <article class="standard">
      <h3>2. Learning activities are aligned, available and engaging</h3>
      <table class="levels">
        <tr><th>Threshold</th><td>Constructively aligned learning activities are available online</td></tr>
        <tr><th>Good</th><td>Learning activities use a variety of appropriate technologies to engage students and support diversity</td></tr>
        <tr class="excellent"><th>Excellent</th><td></td></tr>
      </table>
    </article>
    <article class="standard">
      <h3>3. Assessment tasks are aligned, available and engaging</h3>
      <table class="levels">
        <tr><th>Threshold</th><td>Constructively aligned assessment tasks are available online</td></tr>
        <tr><th>Good</th><td>Assessment tasks use a variety of appropriate technologies to engage students and support diversity</td></tr>
        <tr class="excellent"><th>Excellent</th><td></td></tr>
      </table>
    </article>
    <article class="standard">
      <h3>4. Students are provided with timely, improvement focused formative feedback</h3>
      <table class="levels">
        <tr><th>Threshold</th><td>Appropriate technologies are used to provide students with formative feedback in a timely manner</td></tr>
        <tr><th>Good</th><td>Feedback is provided in a variety of media to engage students and support diversity</td></tr>
        <tr class="excellent"><th>Excellent</th><td></td></tr>
      </table>
    </article>
    <article class="standard">
      <h3>5. Students are provided with opportunities to interact with peers</h3>
      <table class="levels">
        <tr><th>Threshold</th><td>There are opportunities for social interaction</td></tr>
        <tr><th>Good</th><td>There are opportunities for learning-focused interaction</td></tr>
        <tr class="excellent"><th>Excellent</th><td></td></tr>
      </table>
    </article>
    <article class="standard">
      <h3>6. Students are provided with opportunities to interact with staff</h3>
      <table class="levels">
        <tr><th>Threshold</th><td>Staff are provided with opportunities to answer student queries</td></tr>
        <tr><th>Good</th><td>Staff are provided with opportunities to be active participants in learning-focused interactions</td></tr>
        <tr class="excellent"><th>Excellent</th><td></td></tr>
      </table>
    </article>
    <article class="standard">
      <h3>7. Students are provided with appropriate learning support</h3>
      <table class="levels">
        <tr><th>Threshold</th><td>Appropriate, up-to-date and reliable learning guides and resources are provided online</td></tr>
        <tr><th>Good</th><td>A range of appropriate, up-to-date and reliable online learning skills workshops are available</td></tr>
        <tr class="excellent"><th>Excellent</th><td></td></tr>
      </table>
    </article>
  </div>

  <div class="column col-b">
    <article class="standard">
      <h3>8. Students are supported in their use of educational technology</h3>
      <table class="levels">
        <tr><th>Threshold</th><td>Appropriate, up-to-date and reliable technological guides and resources are provided online</td></tr>
        <tr><th>Good</th><td>Appropriate, timely and reliable asynchronous technological support is available</td></tr>
        <tr class="excellent"><th>Excellent</th><td></td></tr>
      </table>
    </article>

    <section class="theme-box theme-staff">
      <h2 class="theme-title">Two: Staff</h2>
      <p class="theme-summary">Staff are supported in their online teaching with quality professional development [9], resourcing [10] and technical support [11].</p>
    </section>

    <article class="standard">
      <h3>9. Staff are provided with quality professional development in online education</h3>
      <table class="levels">
        <tr><th>Threshold</th><td>A range of appropriate, up-to-date and informative professional development activities are available to staff</td></tr>
        <tr><th>Good</th><td>The organisation requires staff to engage in continued professional development relevant to online education</td></tr>
        <tr class="excellent"><th>Excellent</th><td></td></tr>
      </table>
    </article>
    <article class="standard">
      <h3>10. Online education is recognised in workload</h3>
      <table class="levels">
        <tr><th>Threshold</th><td>Online teaching is recognised in workload</td></tr>
        <tr><th>Good</th><td>Online unit development is recognised in workload</td></tr>
        <tr class="excellent"><th>Excellent</th><td></td></tr>
      </table>
    </article>
    <article class="standard">
      <h3>11. Staff are supported in their use of educational technology</h3>
      <table class="levels">
        <tr><th>Threshold</th><td>Appropriate, up-to-date and reliable technological guides and resources are provided online</td></tr>
        <tr><th>Good</th><td>Appropriate, timely and reliable asynchronous technological support is available</td></tr>
        <tr class="excellent"><th>Excellent</th><td></td></tr>
      </table>
    </article>

    <div class="licence-mark"><span class="dot"></span><span class="name">open share</span></div>
    <div class="licence-note">
      <p>This work is licensed under the Open Share Attribution-ShareAlike 3.0 Unported License. To view a copy of this license, visit http://opensharetrust.org/licenses/by-sa/3.0/ or send a letter to Open Share Trust, 18 Harbour Lane, Suite 40, Fenwick, California, 90210, USA.</p>
      <p>Support for this activity has been provided by the National Office for Tertiary Teaching. The views expressed in this activity do not necessarily reflect the views of the National Office for Tertiary Teaching.</p>
    </div>
  </div>

  <div class="column col-c">
    <article class="standard">
      <h3>12. The organisation provides strategic leadership in online education</h3>
      <table class="levels">
        <tr><th>Threshold</th><td>The organisation has a clearly articulated strategic position on online education</td></tr>
        <tr><th>Good</th><td>An appropriate member of the executive has explicit responsibility for online education</td></tr>
        <tr class="excellent"><th>Excellent</th><td></td></tr>
      </table>
    </article>
    <article class="standard">
      <h3>13. The organisation employs a systematic approach to resource allocation in online education</h3>
      <table class="levels">
        <tr><th>Threshold</th><td>There is a systematic approach to resource allocation</td></tr>
        <tr><th>Good</th><td>There is systematic approach with formal criteria that are widely available</td></tr>
        <tr class="excellent"><th>Excellent</th><td></td></tr>
      </table>
    </article>
    <article class="standard">
      <h3>14. The organisation maintains and supports a quality learning platform for delivering online education</h3>
      <table class="levels">
        <tr><th>Threshold</th><td>The organisation maintains and supports an appropriate learning platform</td></tr>
        <tr><th>Good</th><td>The learning platform provided is fit for purpose, scalable and reliable</td></tr>
        <tr class="excellent"><th>Excellent</th><td></td></tr>
      </table>
    </article>
    <article class="standard">
      <h3>15. The organisation has a process for evaluating and improving student satisfaction with online education</h3>
      <table class="levels">
        <tr><th>Threshold</th><td>The organisation has a systematic process for evaluating and improving student satisfaction with online education</td></tr>
        <tr><th>Good</th><td>The organisation has a systematic process for improving student learning outcomes and satisfaction with online education and communicating improvements to students</td></tr>
        <tr class="excellent"><th>Excellent</th><td></td></tr>
      </table>
    </article>
    <article class="standard">
      <h3>16. The organisation has a process for evaluating and improving training and support for staff</h3>
      <table class="levels">
        <tr><th>Threshold</th><td>The organisation has a systematic process for evaluating and improving staff training and support</td></tr>
        <tr><th>Good</th><td>The organisation has a systematic process for improving staff training and support and communicating improvements to staff</td></tr>
        <tr class="excellent"><th>Excellent</th><td></td></tr>
      </table>
    </article>
    <article class="standard">
      <h3>17. The organisation has a process for evaluating and improving infrastructure</h3>
      <table class="levels">
        <tr><th>Threshold</th><td>The organisation has a systematic process for evaluating and improving infrastructure</td></tr>
        <tr><th>Good</th><td>The organisation has a systematic process for improving infrastructure and communicating improvements to stakeholders</td></tr>
        <tr class="excellent"><th>Excellent</th><td></td></tr>
      </table>
    </article>
  </div>
</main>
</body>
</html>
```